Author needs a new book, Kindle and Audiobook cover design

I updated and re-edited a book I wrote 25 years ago but now realize the title and design did not get the job done. I am seeking a book, Kindle and audiobook design that will make me stand out. The final design will pop while being sensitive to the nature of the subject. The title of the book is Quiet Lanterns. Subtitle: Ways to Notice and Step Away From Harmful Circles While Keeping Steady Belief by Dorian T. Wexcombe. I am wanting to get the attention of people who have been damaged by a church relationship that started well but ended badly.
Updates

The book title is: Quiet Lanterns. The Subtitle is: Ways To Notice and Step Away From Harmful Circles While Keeping Steady Belief. The dimension is 6x9 (150 pages) and I am the author: Dorian T. Wexcombe

Target Market(s)

People with a church experience; church leadership. Religious abuse victims.

Industry/Entity Type

Christian

Font styles to use
Serif

Colors

Designer to choose colors to be used in the design.

Requirements
Nice to have
• I am not married to the Serif font if another design works better.

```html
<!DOCTYPE html>
<html lang="en">
<head>
<meta charset="utf-8">
<title>Quiet Lanterns — Cover Wrap</title>
<link rel="stylesheet" href="https://fonts.googleapis.com/css2?family=Roboto:ital,wght@0,400;0,500;0,700;0,900;1,400;1,700&display=swap">
<style>
  :root {
    --page: #ffffff;
    --frame-edge: #d9d9d9;
    --cover-dark: #2a2a2a;
    --spine-dark: #262626;
    --panel: rgba(70, 70, 70, 0.78);
    --ink-light: #ffffff;
    --ink-dark: #1c1c1c;
    --accent-red: #ee1c1c;
    --rule: #cfcfcf;
  }
  * { margin: 0; padding: 0; box-sizing: border-box; }
  html, body { width: 1200px; height: 874px; overflow: hidden; background: var(--page); }
  .canvas {
    position: relative; width: 1200px; height: 874px;
    background: var(--page);
    border: 2px solid var(--frame-edge);
    font-family: "Roboto", Arial, sans-serif;
  }
  .wrap { position: absolute; left: 31px; top: 24px; width: 1141px; height: 828px; }

  /* Back cover */
  .back {
    position: absolute; left: 0; top: 0; width: 554px; height: 828px;
    background: linear-gradient(180deg, #bdbdbd 0%, #9a9a9a 40%, #5e5e5e 62%, #7a7a7a 72%, #3a3a3a 100%);
  }
  .endorsements {
    position: absolute; left: 20px; top: 23px; width: 513px; height: 631px;
    background: var(--panel);
    color: var(--ink-light);
    padding: 20px 22px 0;
    text-align: center;
  }
  .quote { font-style: italic; font-size: 13.4px; line-height: 17.5px; }
  .credit { font-size: 13.4px; line-height: 17.5px; margin-top: 10px; }
  .endorsement + .endorsement { margin-top: 22px; }
  .endorsement:nth-child(3) { margin-top: 34px; }
  .endorsement:nth-child(4) { margin-top: 32px; }

  .author-photo {
    position: absolute; left: 70px; top: 667px; width: 126px; height: 126px;
    border-radius: 50%; border: 3px solid #8a8a8a;
    background: radial-gradient(circle at 50% 45%, #d9a58f 0%, #b97f6a 45%, #5a5a5a 100%);
  }
  .bio {
    position: absolute; left: 180px; top: 662px; width: 339px; height: 141px;
    background: var(--ink-light); color: var(--ink-dark);
    padding: 16px 18px; text-align: center;
    font-style: italic; font-size: 13.4px; line-height: 17.5px;
  }

  /* Spine */
  .spine {
    position: absolute; left: 554px; top: 0; width: 33px; height: 828px;
    background: var(--spine-dark);
  }
  .spine-title, .spine-author {
    position: absolute; left: 50%; white-space: nowrap;
    transform-origin: 0 0; transform: rotate(90deg) translateY(-50%);
    font-weight: 500; letter-spacing: 0.5px;
  }
  .spine-title { top: 84px; color: var(--accent-red); font-size: 24px; font-weight: 700; }
  .spine-author { top: 467px; color: var(--ink-light); font-size: 19px; font-weight: 700; letter-spacing: 1.5px; }

  /* Front cover */
  .front {
    position: absolute; left: 587px; top: 0; width: 554px; height: 828px;
    background: var(--cover-dark); overflow: hidden;
  }
  .front-author {
    position: absolute; top: 43px; left: 0; width: 100%; padding-left: 26px;
    text-align: center; color: var(--ink-light);
    font-weight: 700; font-size: 19px; letter-spacing: 1.6px;
  }
  .veiled-figure {
    position: absolute; left: 70px; top: 107px; width: 440px; height: 721px;
    background: radial-gradient(ellipse 60% 70% at 50% 55%, #cfcfcf 0%, #9c9c9c 45%, #5a5a5a 75%, rgba(42,42,42,0) 100%);
    border-radius: 48% 52% 0 0 / 30% 30% 0 0;
  }
  .title {
    position: absolute; left: 41px; top: 568px;
    color: var(--accent-red); font-weight: 900;
    font-size: 74px; line-height: 67px; letter-spacing: -0.5px;
  }
  .title-rule {
    position: absolute; left: 41px; top: 717px; width: 472px; height: 2px;
    background: var(--rule);
  }
  .subtitle {
    position: absolute; left: 41px; top: 730px;
    color: var(--ink-light); font-style: italic; font-weight: 700;
    font-size: 17.5px; line-height: 23.5px;
  }
</style>
</head>
<body>
<div class="canvas">
  <div class="wrap">

    <section class="back">
      <div class="endorsements">
        <div class="endorsement">
          <p class="quote">Dorian Wexcombe offers expert insight and a transparent evaluation in this book. With years of healthy involvement with that which is right in the body of Christ, he can speak to both the personal and systematic issues that cause bad environments to develop. The church landscape is littered with people who have been hurt in churches. This book will help clean things up.</p>
          <p class="credit">–Malcolm Treadway, Senior Pastor, Cedar Hollow Fellowship, Ashford, VT.<br>Cedarhollowfc.org</p>
        </div>
        <div class="endorsement">
          <p class="quote">“Seldom, if ever, have<br>I read a book that was so refreshingly personal and real, yet delivered material that put you in a position to navigate the difficult and damaging challenges, of being part of a degenerating church. I was moved to tears and then lifted to a place of hope, by the pain and abuse that this family faced and their incredible testimony and journey of recovery. All glory to the power of His love for us.”</p>
          <p class="credit">– Piet Vosloo, Kestrel Outreach, easternpathwaysjourney.com</p>
        </div>
        <div class="endorsement">
          <p class="quote">“Dorian Wexcombe offers a real-world view on how following your spiritual calling is not always easy but completely worth the journey. His down to earth approach allows the reader to process and be encouraged by his personal story, insight, and commitment to faith.”</p>
          <p class="credit">-- Lydia Marchetti, Executive Director, Harborlight Ministry, Inc. Harborlight.org</p>
        </div>
        <div class="endorsement">
          <p class="quote">“Dorian Wexcombe has been a pastor over 40 years. I have known him personally for many of those years. This book is a case study of how trust can be abused. Dorian handles this difficult issue with a good balance of honest introspection and critical analysis of leadership structures and practices. This book is a must-read.”</p>
          <p class="credit">-- --Russell K. Ambrose, ReasonedFaithDesk.com</p>
        </div>
      </div>

      <div class="author-photo" role="img" aria-label="Portrait photograph of the author"></div>
      <p class="bio">Dorian Wexcombe is a long-time pastor, author and podcaster who has impacted leaders and churches for many years. He wrote Iceberg Ahead, a study of church leadership drawn from the history of the legendary ship. He and his wife Helena, together with their grown children and spouses all serve in ministry.</p>
    </section>

    <section class="spine">
      <span class="spine-title">QUIET LANTERNS</span>
      <span class="spine-author">Dorian T. Wexcombe</span>
    </section>

    <section class="front">
      <p class="front-author">Dorian T. Wexcombe</p>
      <div class="veiled-figure" role="img" aria-label="Black and white image of a veiled standing figure blended with a small white church and steeple"></div>
      <h1 class="title">QUIET<br>LANTERNS</h1>
      <div class="title-rule"></div>
      <p class="subtitle">Ways To Notice and Step Away<br>From Harmful Circles<br>While Keeping Steady Belief</p>
    </section>

  </div>
</div>
</body>
</html>
```